BrightvaleHR Brochure

We need a Brochure design for a Human Resources company based in Windhoek Namibia. We do general HR admin, payroll, disciplinary hearings, recruitment. We would like a design which can be used to print hardcopies as well as pdf versions.

Industry/Entity Type

Human Resource

Colors

Designer to choose colors to be used in the design.

Requirements
Nice to have
• relevant pictures

```html
<!DOCTYPE html>
<html lang="en">
<head>
<meta charset="utf-8">
<title>BrightvaleHR Brochure</title>
<link rel="stylesheet" href="https://fonts.googleapis.com/css2?family=Arimo:wght@400;700&display=swap">
<style>
  :root {
    --paper: #ffffff;
    --royal-blue: #1b6dbf;
    --charcoal: #3d3d3f;
    --teal-deep: #0e5b6a;
    --teal-mid: #1f8f9c;
    --teal-light: #6fc3cc;
    --navy: #1d3c7a;
    --canvas-bg: #e9e9e9;
    --text-light: #ffffff;
  }
  * { box-sizing: border-box; margin: 0; padding: 0; }
  html, body { width: 1200px; height: 800px; overflow: hidden; background: var(--canvas-bg); }
  body { font-family: "Arimo", Arial, sans-serif; }
  .spread { position: relative; width: 1200px; height: 800px; background: var(--paper); }
  .fold { position: absolute; left: 600px; top: 0; width: 1px; height: 800px; background: rgba(0,0,0,0.08); z-index: 5; }

  /* back page */
  .back-band { position: absolute; left: 0; top: 200px; width: 600px; height: 560px; background: var(--royal-blue); }
  .member-box { position: absolute; left: 60px; top: 222px; width: 330px; height: 278px; background: var(--charcoal); color: var(--text-light); padding: 24px 24px; }
  .member-head { display: flex; gap: 14px; align-items: flex-start; }
  .headshot { width: 60px; height: 70px; background: linear-gradient(160deg, #b88a6a, #5b3b2a); border-bottom: 4px solid var(--royal-blue); flex: none; }
  .member-title { font-weight: 700; font-size: 12px; line-height: 1.3; margin-top: 4px; }
  .member-text, .approach-text { font-size: 12px; line-height: 1.45; text-align: justify; }
  .member-text { margin-top: 12px; }
  .approach-bar { position: absolute; left: 60px; top: 492px; width: 340px; height: 14px; background: var(--royal-blue); }
  .approach-label { position: absolute; left: 78px; top: 514px; color: var(--text-light); font-weight: 700; font-size: 12px; letter-spacing: 0.5px; }
  .approach-box { position: absolute; left: 60px; top: 536px; width: 370px; height: 110px; background: var(--charcoal); color: var(--text-light); padding: 16px 24px; }
  .contact-block { position: absolute; left: 40px; top: 662px; width: 380px; color: var(--text-light); font-size: 13px; line-height: 1.45; text-align: right; font-style: normal; }
  .contact-block strong { font-weight: 700; }

  /* photo area */
  .photo { position: absolute; background: radial-gradient(ellipse at 60% 45%, var(--teal-light) 0%, var(--teal-mid) 40%, var(--teal-deep) 100%); }
  .photo-back { left: 440px; top: 200px; width: 160px; height: 560px; background: linear-gradient(90deg, #2a8fa3, #3ea3b0); }
  .photo-front { left: 600px; top: 160px; width: 600px; height: 500px; }

  /* cover */
  .brand { position: absolute; right: 60px; top: 60px; display: flex; align-items: center; gap: 12px; }
  .brand-dot { width: 34px; height: 34px; border-radius: 50%; background: var(--navy); }
  .brand-name { font-weight: 700; font-size: 30px; color: var(--navy); letter-spacing: 0.5px; }
  .cover-title { position: absolute; right: 70px; top: 520px; text-align: right; color: var(--text-light); z-index: 3; }
  .cover-title .line-1 { font-weight: 700; font-size: 34px; }
  .cover-title .line-2 { font-weight: 400; font-size: 32px; margin-top: 4px; }
</style>
</head>
<body>
<main class="spread">
  <section class="back-page">
    <div class="back-band"></div>
    <div class="photo photo-back" role="img" aria-label="Businessman touching a glowing network of people icons"></div>

    <div class="member-box">
      <div class="member-head">
        <div class="headshot" role="img" aria-label="Portrait of the managing member"></div>
        <p class="member-title">Our Managing Member<br>Mrs Anika Voss</p>
      </div>
      <p class="member-text">We offer a range of HR consulting services, all designed to help your company reach its potential. Whether you're looking for a small tweak or complete overhaul, we have you covered. Our services are available a la carte so you can get precisely what you need.</p>
    </div>

    <div class="approach-bar"></div>
    <p class="approach-label">OUR APPROACH</p>
    <div class="approach-box">
      <p class="approach-text">Each company is unique. One-size-fits-all approaches will never help your business reach its full potential. We deliver custom solutions, tailored to you – your industry, your culture, your one-of-a-kind challenges.</p>
    </div>

    <address class="contact-block">
      P O Box 41120 Maple Court Windhoek Namibia<br>
      Cellphone <strong>+264 81 555 0142</strong><br>
      E-mail <strong>anika@brightvalehr.com</strong><br>
      www.brightvalehr.com
    </address>
  </section>

  <div class="fold"></div>

  <section class="cover-page">
    <div class="brand">
      <span class="brand-dot"></span>
      <span class="brand-name">BrightvaleHR</span>
    </div>
    <div class="photo photo-front" role="img" aria-label="Businessman holding a tablet and touching a glowing network of people icons"></div>
    <h1 class="cover-title">
      <div class="line-1">Brightvale</div>
      <div class="line-2">Human Resources CC</div>
    </h1>
  </section>
</main>
</body>
</html>
```